Help designing a web admin portal for cloud access control company

Hello, we need help to design our web admin portal for our cloud based access control product called halcyon gatekeep. Please see the attached admin portal wireframe. this is not absolute so we are open to UX / UI suggestions. This web admin portal will allow a admin at a small to medium sized business add new employees to their access control system and grant different access.
Updates

Project Deadline Extended
Reason: Waiting in a couple designs for people that said they would send something in

Target Market(s)

B2B

Industry/Entity Type

It Company

Font styles to use
Sans Serif

Colors
3277b5

Requirements
Must have
• Very simple and clean design. we like clean fonts like Oswald extra light. Please see an image of the wining app designs to see what the color and styling should look like

```html
<!DOCTYPE html>
<html lang="en">
<head>
<meta charset="utf-8">
<title>Halcyon Gatekeep — Reports</title>
<link rel="stylesheet" href="https://fonts.googleapis.com/css2?family=Oswald:wght@200;300;400&display=swap">
<style>
:root{
  --ink-dark:#333333;
  --brand-blue:#0a70c0;
  --sky-blue:#5aa5d8;
  --mid-blue:#3a8ccb;
  --title-blue:#4a9fd8;
  --frame-blue:#7fb6e0;
  --cyan:#2ec4e6;
  --green:#26b574;
  --pie-grey:#4a4a4a;
  --text-grey:#555555;
  --rule-grey:#d6d6d6;
  --white:#ffffff;
}
*{box-sizing:border-box;margin:0;padding:0}
html,body{width:1200px;height:1000px;overflow:hidden;background:var(--white);font-family:'Oswald',sans-serif;font-weight:300}
.portal{position:relative;width:1200px;height:1000px}
.topbar{position:absolute;left:0;top:74px;width:1200px;height:74px;background:var(--ink-dark);color:var(--white)}
.brand{position:absolute;left:34px;top:17px;display:flex;align-items:center;gap:6px;font-size:21px;font-weight:300}
.brand-dot{width:30px;height:30px;border-radius:50%;background:var(--sky-blue)}
.welcome{position:absolute;right:38px;top:22px;font-size:18px}
.sidebar{position:absolute;left:0;top:148px;width:226px;height:772px;background:var(--ink-dark);color:var(--white)}
.menu-toggle{position:absolute;left:36px;top:17px;width:26px}
.menu-toggle span{display:block;height:2px;background:var(--white);margin-bottom:4px}
.nav{list-style:none;position:absolute;top:80px;left:0;width:226px}
.nav li{height:42.3px;line-height:31px;padding:0 35px;font-size:18px;text-transform:uppercase}
.nav li.active{background:var(--sky-blue);height:39px;line-height:39px;margin-top:-4px;margin-bottom:7px}
.today{position:absolute;left:28px;bottom:20px;font-size:15px;text-decoration:underline}
.doorbar{position:absolute;left:226px;top:148px;width:974px;height:49px;background:var(--brand-blue);border-top:1px solid #2a8ad0}
.door-label{position:absolute;left:154px;top:0;width:180px;height:49px;background:var(--sky-blue);color:var(--white);font-size:18px;line-height:46px;padding-left:22px}
.door-label::after{content:"";position:absolute;right:-14px;top:12px;border-left:14px solid var(--sky-blue);border-top:12px solid transparent;border-bottom:12px solid transparent}
.door-group{position:absolute;left:334px;top:0;width:467px;height:49px;background:var(--mid-blue)}
.door{position:absolute;top:8px;display:flex;align-items:center;gap:8px;color:var(--white);font-size:12px;line-height:14px}
.door-switch{width:44px;height:30px;background:var(--white)}
.door-switch.on{background:var(--sky-blue);border:2px solid var(--white)}
.reports-head{position:absolute;left:300px;top:236px;width:815px;height:38px;border-bottom:1px solid var(--title-blue)}
.reports-head h1{font-size:28px;font-weight:300;color:var(--title-blue);line-height:36px}
.tools{position:absolute;right:0;top:-7px;display:flex;border:1px solid var(--frame-blue)}
.tool{width:43px;height:42px;display:flex;align-items:center;justify-content:center}
.tool+.tool{border-left:1px solid var(--frame-blue)}
.date-field{position:absolute;top:292px;height:38px;border:1px solid var(--frame-blue);color:#8a8a8a;font-size:15px;line-height:36px;padding-left:14px}
.date-field::after{content:"";position:absolute;right:14px;top:16px;border-top:7px solid #a08c78;border-left:6px solid transparent;border-right:6px solid transparent}
.date-dash{position:absolute;left:621px;top:300px;color:var(--text-grey);font-size:18px}
.data-panel{position:absolute;left:305px;top:349px;width:811px;height:297px;border:1px solid var(--frame-blue);overflow:hidden}
.data-table{border-collapse:collapse;table-layout:fixed;width:792px;font-size:16px;color:var(--text-grey)}
.data-table th{background:var(--brand-blue);color:var(--white);font-weight:300;height:33px;border-top:2px solid var(--brand-blue)}
.data-table td{height:38.3px;text-align:center;border-right:1px solid #9a9a9a;border-bottom:1px solid var(--rule-grey)}
.scroll-track{position:absolute;right:0;top:33px;width:18px;height:264px;background:#ececec}
.scroll-thumb{position:absolute;left:1px;top:26px;width:16px;height:182px;background:#b0b0b0}
.chart-panel{position:absolute;left:305px;top:653px;width:811px;height:238px;border:1px solid var(--frame-blue)}
.baseline{position:absolute;left:0;top:920px;width:1200px;height:1px;background:var(--rule-grey)}
</style>
</head>
<body>
<div class="portal">
  <header class="topbar">
    <div class="brand"><span class="brand-dot"></span>Halcyon Gatekeep</div>
    <div class="welcome">Welcome, Dale!</div>
  </header>

  <aside class="sidebar">
    <div class="menu-toggle"><span></span><span></span><span></span></div>
    <ul class="nav">
      <li>Home</li><li>Dashboard</li><li>Controller</li><li>Doors</li><li>Employees</li>
      <li>Open/ Close Times</li><li>Cameras</li><li>Time Cards</li><li class="active">Reports</li><li>Settings</li>
    </ul>
    <div class="today">SUNDAY, 11 / 27 / 16</div>
  </aside>

  <div class="doorbar">
    <div class="door-label">Manual Door Opening</div>
    <div class="door-group">
      <div class="door" style="left:40px">Main<br>Door<span class="door-switch on"></span></div>
      <div class="door" style="left:142px">Back<br>Door<span class="door-switch"></span></div>
      <div class="door" style="left:240px">Exec<br>Office<span class="door-switch"></span></div>
      <div class="door" style="left:344px">Storage<br>Room<span class="door-switch"></span></div>
    </div>
  </div>

  <section class="reports-head">
    <h1>Reports</h1>
    <div class="tools">
      <div class="tool"><svg width="22" height="18" viewBox="0 0 22 18"><path d="M2 5v11h16v-4" fill="none" stroke="#3a8ccb" stroke-width="2"/><path d="M7 12c1-5 5-7 10-7V2l5 5-5 5V8c-4 0-7 1-10 4z" fill="#3a8ccb"/></svg></div>
      <div class="tool"><svg width="22" height="20" viewBox="0 0 22 20"><rect x="5" y="1" width="12" height="5" fill="#3a8ccb"/><rect x="1" y="6" width="20" height="9" rx="2" fill="#3a8ccb"/><rect x="5" y="12" width="12" height="7" fill="#fff" stroke="#3a8ccb" stroke-width="2"/></svg></div>
    </div>
  </section>

  <div class="date-field" style="left:301px;width:296px">[ From Date ]</div>
  <div class="date-dash">-</div>
  <div class="date-field" style="left:655px;width:288px">[ To Date ]</div>

  <section class="data-panel">
    <table class="data-table">
      <colgroup><col style="width:103px"><col style="width:89px"><col style="width:91px"><col style="width:91px"><col style="width:92px"><col style="width:89px"><col style="width:90px"><col style="width:91px"><col style="width:56px"></colgroup>
      <thead><tr><th>Caption 1</th><th>Caption 2</th><th>Caption 3</th><th>Caption 3</th><th>Caption 4</th><th>Caption 4</th><th>Caption 4</th><th>Caption 5</th><th></th></tr></thead>
      <tbody>
        <tr><td>Value 1</td><td>Value 2</td><td>Value 3</td><td>Value 3</td><td>Value 4</td><td>Value 4</td><td>Value 4</td><td>Value 4</td><td></td></tr>
        <tr><td>Value 1</td><td>Value 2</td><td>Value 3</td><td>Value 3</td><td>Value 4</td><td>Value 4</td><td>Value 4</td><td>Value 4</td><td></td></tr>
        <tr><td>Value 1</td><td>Value 2</td><td>Value 3</td><td>Value 3</td><td>Value 4</td><td>Value 4</td><td>Value 4</td><td>Value 4</td><td></td></tr>
        <tr><td>Value 1</td><td>Value 2</td><td>Value 3</td><td>Value 3</td><td>Value 4</td><td>Value 4</td><td>Value 4</td><td>Value 4</td><td></td></tr>
        <tr><td>Value 1</td><td>Value 2</td><td>Value 3</td><td>Value 3</td><td>Value 4</td><td>Value 4</td><td>Value 4</td><td>Value 4</td><td></td></tr>
        <tr><td>Value 1</td><td>Value 2</td><td>Value 3</td><td>Value 3</td><td>Value 4</td><td>Value 4</td><td>Value 4</td><td>Value 4</td><td></td></tr>
        <tr><td>Value 1</td><td>Value 2</td><td>Value 3</td><td>Value 3</td><td>Value 4</td><td>Value 4</td><td>Value 4</td><td>Value 4</td><td></td></tr>
      </tbody>
    </table>
    <div class="scroll-track"><div class="scroll-thumb"></div></div>
  </section>

  <section class="chart-panel">
    <svg width="811" height="238" viewBox="305 653 811 238" font-family="Oswald, sans-serif">
      <circle cx="432" cy="772" r="78" fill="var(--pie-grey)" stroke="var(--cyan)" stroke-width="1"/>
      <g stroke="var(--cyan)" stroke-width="1">
        <line x1="432" y1="772" x2="432" y2="694"/>
        <line x1="432" y1="772" x2="445.5" y2="695.2"/>
        <line x1="432" y1="772" x2="471" y2="704.5"/>
        <line x1="432" y1="772" x2="505.3" y2="745.3"/>
        <line x1="432" y1="772" x2="393" y2="839.5"/>
        <line x1="432" y1="772" x2="358.7" y2="745.3"/>
      </g>
      <g fill="#555" font-size="14" font-weight="300">
        <text x="418" y="684">10</text><text x="443" y="685">20</text><text x="492" y="708">40</text>
        <text x="491" y="852">140</text><text x="340" y="834">80</text><text x="352" y="716">70</text>
      </g>
      <g fill="#1e9fd6" font-size="14" font-weight="400" text-anchor="end">
        <text x="595" y="694">25</text><text x="595" y="727">20</text><text x="595" y="759">15</text>
        <text x="595" y="792">10</text><text x="595" y="824">5</text><text x="595" y="857">0</text>
      </g>
      <g stroke="#1e9fd6" stroke-width="2">
        <line x1="602" y1="688" x2="602" y2="852"/>
        <line x1="602" y1="852" x2="1077" y2="852"/>
        <line x1="602" y1="689" x2="611" y2="689"/><line x1="602" y1="722" x2="611" y2="722"/>
        <line x1="602" y1="754" x2="611" y2="754"/><line x1="602" y1="787" x2="611" y2="787"/>
        <line x1="602" y1="819" x2="611" y2="819"/>
      </g>
      <g fill="var(--green)" stroke="#1e9fd6" stroke-width="0.5">
        <rect x="608" y="845" width="35" height="6"/>
        <rect x="655" y="754" width="35" height="97"/>
        <rect x="703" y="819" width="35" height="32"/>
        <rect x="750" y="793" width="35" height="58"/>
        <rect x="798" y="786" width="35" height="65"/>
        <rect x="846" y="832" width="35" height="19"/>
        <rect x="893" y="721" width="35" height="130"/>
        <rect x="941" y="806" width="35" height="45"/>
        <rect x="988" y="689" width="35" height="162"/>
        <rect x="1036" y="773" width="35" height="78"/>
      </g>
    </svg>
  </section>

  <div class="baseline"></div>
</div>
</body>
</html>
```